Harrowgate Legal

To update and modernize current business card appearance. Marisa's business is based in Melbourne with 4 other lawyers in the firm. Marisa travels to the Pilbara in Western Australia approximately 1 week a month as part of the firms legal work. She consults with clients in Newman, Tom Price and Port Hedland. The lawyers work mostly from a home office, apart from court appearances. They have a virtual office in Melbourne city, and use facilities in 3 or 4 other locations around Melbourne. It is important the client's think this is a conventional law firm with a permanent office. Our business structure is a difficult concept for them to grasp. The business has been operational for 3 years, growing from 1 lawyer to 4 lawyers during that time. Our website is www.Harrowgatelegal.com.au and is currently being upgraded as we are not happy with its content. The logo is currently orange and dark grey but the orange is a difficult colour to reproduce and often turns out "poo" brown when documents are printed. We need clients to know we are user friendly and caring - and not head up our rears ends as some lawyers appear to be.
Updates

Thank you for the feedback so far. 1. Some of the designs have too much black (We prefer darker grey & not too much.) 2. Happy for designers to play around with different colours & logo design. What we're after is a modern look and business card that people say "wow" when they pick it up.

Industry/Entity Type

Business

```html
<!DOCTYPE html>
<html lang="en">
<head>
<meta charset="utf-8">
<title>Harrowgate Legal – Business Card</title>
<link href="https://fonts.googleapis.com/css2?family=Roboto:wght@400;500;700&display=swap" rel="stylesheet">
<style>
  :root{
    --stage:#e9e6e1;
    --card-white:#fbfbfb;
    --ink:#3d3d3f;
    --ink-soft:#555557;
    --brand-blue:#2a6aa8;
    --blue-light:#3a8fd0;
    --blue-deep:#15528f;
    --band-grey:#333336;
    --white:#ffffff;
  }
  *{box-sizing:border-box;margin:0;padding:0}
  html,body{width:1200px;height:1023px;overflow:hidden}
  body{
    background:var(--stage);
    font-family:"Roboto",Arial,sans-serif;
    position:relative;
  }
  .card{
    position:absolute;
    width:520px;height:300px;
    border-radius:16px;
    overflow:hidden;
    box-shadow:0 6px 18px rgba(0,0,0,.18);
  }
  /* ---------- front ---------- */
  .card-front{left:45px;top:362px;background:var(--card-white);color:var(--ink)}
  .brand{
    position:absolute;display:flex;align-items:center;gap:10px;
    font-weight:500;font-size:22px;letter-spacing:.5px;
  }
  .brand-dot{width:14px;height:14px;border-radius:50%;display:block}
  .card-front .brand{left:34px;top:38px;color:var(--brand-blue)}
  .card-front .brand-dot{background:var(--brand-blue)}
  .person{position:absolute;right:34px;top:36px;text-align:right}
  .person-name{font-weight:700;font-size:17px;letter-spacing:.3px;color:var(--ink)}
  .person-title{font-size:12.5px;color:var(--brand-blue);margin-top:4px}
  .contact{position:absolute;left:34px;bottom:34px;font-size:12.5px;color:var(--ink-soft);line-height:1.55}
  .contact-row{display:flex;align-items:center;gap:7px}
  .contact-row svg{width:12px;height:12px;flex:none}
  .website{position:absolute;right:34px;bottom:34px;font-size:12.5px;color:var(--ink-soft)}
  .edge-tab{position:absolute;left:0;bottom:0;width:130px;height:8px;background:var(--brand-blue)}
  /* ---------- back ---------- */
  .card-back{
    left:635px;top:362px;color:var(--white);
    background:linear-gradient(135deg,var(--blue-deep) 0%,var(--blue-light) 55%,var(--brand-blue) 100%);
  }
  .card-back .brand{left:34px;top:38px;color:var(--white)}
  .card-back .brand-dot{background:var(--white)}
  .region{position:absolute;right:34px;top:34px;text-align:right;font-weight:700;font-size:16px;line-height:1.3}
  .practice{position:absolute;left:34px;top:128px;font-size:12.5px;line-height:1.6}
  .practice-heading{font-weight:700;font-size:14px;letter-spacing:.4px;margin-bottom:4px}
  .sep{opacity:.8;margin:0 5px}
  .footer-band{
    position:absolute;left:0;right:0;bottom:0;height:46px;
    background:var(--band-grey);
    display:flex;align-items:center;padding:0 34px;
    font-size:12px;letter-spacing:.2px;
  }
</style>
</head>
<body>

<section class="card card-front">
  <div class="brand"><span class="brand-dot"></span>Harrowgate Legal</div>
  <div class="person">
    <div class="person-name">J. MARISA PENROSE</div>
    <div class="person-title">LLB (Hons) - Accredited Mediator</div>
  </div>
  <div class="contact">
    <div>RM 2207 Kestrel Trade Bldg 416</div>
    <div>Larkspur Rd Eastfield VIC</div>
    <div class="contact-row">
      <svg viewBox="0 0 12 12"><path d="M2 1h3l1 3-2 1a7 7 0 0 0 3 3l1-2 3 1v3c-6 0-10-4-10-9z" fill="var(--brand-blue)"/></svg>
      1300 555 018 (1300 Harrowgate)
    </div>
    <div class="contact-row">
      <svg viewBox="0 0 12 12"><rect x="3" y="0.5" width="6" height="11" rx="1" fill="none" stroke="var(--brand-blue)" stroke-width="1.2"/></svg>
      0400 555 217
    </div>
    <div class="contact-row">
      <svg viewBox="0 0 12 12"><rect x="0.5" y="2" width="11" height="8" fill="var(--brand-blue)"/><path d="M1 2.5l5 4 5-4" fill="none" stroke="#fff" stroke-width="1"/></svg>
      marisa.penrose@harrowgatelegal.com.au
    </div>
  </div>
  <div class="website">www.Harrowgatelegal.com.au</div>
  <div class="edge-tab"></div>
</section>

<section class="card card-back">
  <div class="brand"><span class="brand-dot"></span>Harrowgate Legal</div>
  <div class="region">Melbourne Eastern<br>And Bayside Suburbs</div>
  <div class="practice">
    <div class="practice-heading">AREAS OF PRACTICE</div>
    <div>Family Law<span class="sep">|</span>Intervention Orders<span class="sep">|</span>Collaborative Practice</div>
    <div>Criminal Law<span class="sep">|</span>Mediation &amp; Negotiation</div>
  </div>
  <div class="footer-band">Experience • Support • Solutions<span class="sep">|</span>Inquiries : info@harrowgatelegal.com.au</div>
</section>

</body>
</html>
```